Holvik Cabinets Quality Custom Built Kitchens, Vanity Units, Robes ect

Hi,
Was after a new design for our business cards,
we are a cabinet making business and pride ourselves in quality custom built Kitchens, Vanity units, robes ect.
we have been around for over 20 years and we are trying to modernize our card logo.
Looking for something eye catching, bold and exciting
family ran and operated business, we work with builders and also have a large private clientel.

Thanks

Industry/Entity Type

Business

Contact Information for Business Card

Holvik Cabinets

Font styles to use
Serif
Script

Requirements
Must have
• Corinne 0461735928 hvcabinets@mailvane.com
• Po Box 2786
• 5B Wattlebark Court Kelvale Vic 3852
• Phone (03)59286417 Fax (03) 59286942
Nice to have
• Quality Custom Built Kitchens & Vanity Units

```html
<!DOCTYPE html>
<html lang="en">
<head>
<meta charset="utf-8">
<title>Holvik Cabinets – Business Card</title>
<link rel="stylesheet" href="https://fonts.googleapis.com/css2?family=Exo+2:wght@500;700&family=Open+Sans:wght@400;600&display=swap">
<style>
  :root {
    --brand-blue: #1f4596;
    --rule-grey: #808285;
    --ink: #1a1a1a;
    --card-white: #ffffff;
    --backdrop: #e9e7e4;
  }
  * { margin: 0; padding: 0; box-sizing: border-box; }
  html, body { width: 1200px; height: 1000px; overflow: hidden; }
  body { background: var(--backdrop); position: relative; font-family: "Open Sans", Arial, sans-serif; }

  .business-card {
    position: absolute; left: 100px; top: 201px;
    width: 1001px; height: 598px;
    background: var(--card-white);
    border-radius: 28px;
    overflow: hidden;
    box-shadow: 0 6px 18px rgba(0,0,0,0.18);
  }

  .brand {
    position: absolute; left: 0; right: 0; top: 250px;
    text-align: center;
  }
  .brand-name {
    display: inline-flex; align-items: center; gap: 16px;
    font-family: "Exo 2", Arial, sans-serif; font-weight: 700;
    font-size: 50px; letter-spacing: 2px; line-height: 1;
    color: var(--brand-blue); text-transform: uppercase;
  }
  .brand-mark { width: 34px; height: 34px; background: var(--brand-blue); }
  .brand-tagline {
    margin-top: 8px;
    font-family: "Exo 2", Arial, sans-serif; font-weight: 500;
    font-size: 21px; color: var(--ink); letter-spacing: 0.8px;
  }

  .contact-person {
    position: absolute; right: 531px; top: 428px;
    text-align: right;
  }
  .person-name {
    font-family: "Exo 2", Arial, sans-serif; font-weight: 700;
    font-size: 25px; color: var(--brand-blue); letter-spacing: 1px;
    text-transform: uppercase;
  }
  .person-mobile {
    margin-top: 4px; font-size: 20px; color: var(--ink);
    display: flex; align-items: center; gap: 4px; justify-content: flex-end;
  }
  .person-mobile svg { width: 20px; height: 20px; fill: var(--brand-blue); }

  .contact-divider {
    position: absolute; left: 498px; top: 404px;
    width: 2px; height: 120px; background: var(--rule-grey);
  }

  .contact-details {
    position: absolute; left: 526px; top: 396px;
    list-style: none; font-size: 20px; line-height: 26.5px; color: var(--ink);
  }
  .contact-details li { display: flex; align-items: center; gap: 8px; }
  .contact-details svg { width: 18px; height: 18px; fill: var(--brand-blue); flex: none; }

  .rule-grey {
    position: absolute; left: 0; right: 0; top: 547px; height: 7px;
    background: var(--rule-grey);
  }
  .band-blue {
    position: absolute; left: 0; right: 0; top: 556px; bottom: 0;
    background: var(--brand-blue);
  }
</style>
</head>
<body>
  <article class="business-card">
    <header class="brand">
      <div class="brand-name"><span class="brand-mark"></span>Holvik Cabinets</div>
      <p class="brand-tagline">Quality Custom Built Kitchens &amp; Vanity Units</p>
    </header>

    <div class="contact-person">
      <p class="person-name">Corinne</p>
      <p class="person-mobile">0461735928
        <svg viewBox="0 0 24 24" aria-hidden="true"><path d="M6.6 10.8a15 15 0 0 0 6.6 6.6l2.2-2.2c.3-.3.7-.4 1-.2 1.1.4 2.3.6 3.6.6.6 0 1 .4 1 1V20c0 .6-.4 1-1 1A17 17 0 0 1 3 4c0-.6.4-1 1-1h3.5c.6 0 1 .4 1 1 0 1.3.2 2.5.6 3.6.1.3 0 .7-.2 1z"/></svg>
      </p>
    </div>

    <div class="contact-divider"></div>

    <ul class="contact-details">
      <li>
        <svg viewBox="0 0 24 24" aria-hidden="true"><path d="M2 9c0-3 4.5-5 10-5s10 2 10 5v2h-5V9H7v2H2zM6 12h12l2 8H4zm6 2a2.5 2.5 0 1 0 0 5 2.5 2.5 0 0 0 0-5z"/></svg>
        (03)59286417
      </li>
      <li>
        <svg viewBox="0 0 24 24" aria-hidden="true"><path d="M7 3h10v5H7zM3 9h18v8h-3v-3H6v3H3zm4 6h10v6H7z"/></svg>
        (03) 59286942
      </li>
      <li>
        <svg viewBox="0 0 24 24" aria-hidden="true"><path d="M2 5h20v14H2zm2 2v.5l8 5.5 8-5.5V7l-8 5z"/></svg>
        hvcabinets@mailvane.com
      </li>
      <li>Po Box 2786</li>
      <li>5B Wattlebark Court Kelvale Vic 3852</li>
    </ul>

    <div class="rule-grey"></div>
    <div class="band-blue"></div>
  </article>
</body>
</html>
```